Divorce Resource

I would like someone to set up a very basic website using WORDPRESS for me - to be developed significantly at a later stage.

I will run initially only as a landing page for an advertising campaign that directs people to the website where they will be informed that it is still under construction and that I would like their input to ensure that all of the research and written material answers all of the commonly asked questions and those that are a little outside of the norm. It will capture a user name and email address and then direct them to answer a brief survey. For their input, they will receive a copy of the ebook once it is finished if they check the box requesting it.

My aim is to capture the questions of the folk who answer the ad so as to develop the website to meet their needs and expectations.

I need access to the contact database and survey results. I have a logo already that has a solid colour background and three jigsaw pieces in the graphics (see attached file). Id like to be able to integrate the jigsaw pieces into the design of the overall website. ie "putting all the pieces together to see the big picture".

The site is for information on divorce ... eventually, it will have all manner of info, including a blog, forums, a secure member's area, book reviews and sales through rivenmart affiliate marketing and a shopping cart for independent item sales.

I have a domain name registered and hosting with BrightHostly in Australia which does support Wordpress. I would like my site to look and feel original and project a professional, reliable but up to date and modern approach to the overall event of a divorce. It must allow for banner advertising and ppc advertising.

Obviously, people who submit on this project, will be given first option to submit on subsequent development.

I look forward to hearing from you.

Target Market(s)

Anyone who is contemplating, going through or coming out the other side of a divorce or separation in Australia.

Industry/Entity Type

Construction

Requirements
Must have
• A database that collates email and usernames
A survey facility that I can easily amend
Collection and collation of survey results
Use of existing logo and colour scheme

```html
<!DOCTYPE html>
<html lang="en">
<head>
<meta charset="utf-8">
<title>Piece by Piece Help</title>
<link href="https://fonts.googleapis.com/css2?family=Arimo:wght@400;700&family=Open+Sans:wght@300;400;600&display=swap" rel="stylesheet">
<style>
:root{
  --teal-deep:#0a4f5a;
  --teal:#0e6570;
  --teal-nav:#0f7480;
  --cyan:#3fd2e2;
  --search-fill:#2ab0c2;
  --red:#b3202b;
  --white:#ffffff;
  --panel-a:#d9d9da;
  --panel-b:#c8c8c9;
  --panel-c:#b1b1b2;
  --field:#9c9c9d;
  --ink:#555;
  --ink-dark:#333;
}
*{margin:0;padding:0;box-sizing:border-box}
html,body{width:1200px;height:1108px;overflow:hidden}
body{position:relative;font-family:"Arimo",Arial,sans-serif;background:#eee}
.abs{position:absolute}
.header{left:0;top:0;width:1200px;height:148px;background:linear-gradient(180deg,var(--teal) 0%,var(--teal-deep) 100%)}
.brand{left:40px;top:82px;color:var(--white);font-family:"Arimo",Arial,sans-serif;font-weight:400;font-size:34px;white-space:nowrap}
.search-field{left:744px;top:55px;width:312px;height:45px;border-radius:8px;background:var(--search-fill);color:#bfeef4;font-size:14px;padding:14px 16px}
.search-btn{left:1064px;top:58px;width:82px;height:39px;border-radius:6px;background:linear-gradient(#a8d84c,#6da821);color:#1e3a08;font-size:14px;text-align:center;line-height:39px;box-shadow:0 2px 4px rgba(0,0,0,.35)}
.nav{left:0;top:148px;width:1200px;height:51px;background:var(--teal-nav)}
.nav a{position:absolute;top:16px;color:var(--white);font-weight:700;font-size:16px;text-decoration:none;white-space:nowrap}
.nav a.current{color:#d9f08a}
.hero{left:0;top:199px;width:1200px;height:297px;background:radial-gradient(ellipse at 30% 60%,#17707a 0%,var(--teal-deep) 70%)}
.stage{left:0;top:496px;width:1200px;height:524px;background:linear-gradient(#e4e4e4,#f4f4f4 60%,#fff)}
.ebook-art{left:70px;top:218px;width:275px;height:370px;background:linear-gradient(100deg,#7cbf2a,#c3e87a 55%,#a6d650);border-radius:4px}
.hero-title{left:474px;top:250px;width:600px;color:var(--cyan);font-weight:700;font-size:31px;line-height:49px}
.hero-text{left:474px;top:360px;width:560px;color:var(--white);font-weight:700;font-size:15.5px;line-height:25px}
.buy{top:509px;height:60px;border-radius:7px;background:linear-gradient(#d8424b,var(--red) 55%,#8c141d);color:var(--white);box-shadow:0 2px 4px rgba(0,0,0,.3)}
.buy .label{position:absolute;left:64px;top:15px;font-weight:700;font-size:20px}
.buy .sub{position:absolute;right:16px;top:40px;font-size:11px;font-weight:700;text-decoration:underline}
.buy svg{position:absolute;left:18px;top:13px}
.panel{top:646px;height:309px}
.panel h2{position:absolute;top:22px;width:100%;text-align:center;font-family:"Open Sans",sans-serif;font-weight:400;font-size:25px;color:var(--ink)}
.field{left:78px;width:266px;height:53px;border-radius:8px;background:var(--field);color:#e2e2e2;font-size:15px;padding:17px 18px}
.signin{left:154px;top:883px;width:120px;height:40px;border-radius:6px;background:linear-gradient(#6a5448,#3f2e25);color:var(--white);font-family:"Open Sans",sans-serif;font-size:18px;text-align:center;line-height:40px}
.step{font-size:11px;color:var(--ink-dark)}
.survey-text{left:428px;top:722px;width:347px;font-weight:700;font-size:14px;line-height:25px;color:#666;text-align:justify}
.more{left:688px;top:857px;font-weight:700;font-size:14px;color:#555}
.ebook-icon{left:822px;top:750px;width:93px;height:110px;background:linear-gradient(120deg,#444,#111);border-radius:4px}
.receive{left:937px;top:740px;font-family:"Open Sans",sans-serif;font-size:24px;line-height:40px;color:#333}
.receive-note{left:940px;top:823px;width:210px;font-size:12.5px;line-height:18px;color:#333}
.get{left:968px;top:896px;width:161px;height:41px;border-radius:5px;background:#000;color:var(--white);font-family:"Open Sans",sans-serif;font-size:18px;text-align:center;line-height:41px}
.footer{left:0;top:1020px;width:1200px;height:88px;background:var(--teal-deep)}
.copyright{left:31px;top:1059px;color:var(--white);font-size:12.5px}
.connect{left:848px;top:1059px;color:var(--white);font-size:12.5px}
.social{top:1048px;width:38px;height:38px;border-radius:50%;background:#2b7f8c;color:var(--white);font-size:8px;font-weight:700;text-align:center;line-height:38px}
</style>
</head>
<body>
<header class="abs header"></header>
<div class="abs brand">Piece by Piece Help</div>
<div class="abs search-field">Enter text...</div>
<div class="abs search-btn">SEARCH</div>

<nav class="abs nav">
  <a class="current" style="left:59px">Home</a>
  <a style="left:133px">About us</a>
  <a style="left:234px">Blog</a>
  <a style="left:299px">Forums,</a>
  <a style="left:394px">Members area</a>
  <a style="left:534px">Book reviews</a>
  <a style="left:666px">Rivenmart affiliate marketing</a>
  <a style="left:916px">Shopping cart</a>
  <a style="left:1053px">Contact Us</a>
</nav>

<section class="abs hero"></section>
<div class="abs stage"></div>
<div class="abs ebook-art" role="img" aria-label="Green e-book cover standing upright"></div>

<h1 class="abs hero-title">Sections 1.10.32 and 1.10.33 from de "Finibus Bonorum et Malorum"</h1>
<p class="abs hero-text">Sections 1.10.32 and 1.10.33 from "de Finibus Bonorum et Malorum" by Marcus Vell are also reproduced in their exact original form, accompanied by English versions from the 1914 translation by J. Tornby.</p>

<div class="abs buy" style="left:490px;width:244px">
  <svg width="30" height="30" viewBox="0 0 30 30"><circle cx="15" cy="15" r="14" fill="#fff"/><path d="M12 9l6 6-6 6" stroke="#8c141d" stroke-width="3" fill="none"/></svg>
  <span class="label">Buy as Paperback</span><span class="sub">Purchase</span>
</div>
<div class="abs buy" style="left:755px;width:246px">
  <svg width="30" height="30" viewBox="0 0 30 30"><circle cx="15" cy="15" r="14" fill="#fff"/><path d="M12 9l6 6-6 6" stroke="#8c141d" stroke-width="3" fill="none"/></svg>
  <span class="label">Buy as PDF</span><span class="sub">Purchase</span>
</div>

<svg class="abs" style="left:0;top:0" width="1200" height="1020" viewBox="0 0 1200 1020">
  <path d="M25 646h379v309H66l-41-41z" fill="var(--panel-a)"/>
  <path d="M410 646h380v309H451l-41-41z" fill="var(--panel-b)"/>
  <path d="M796 646h379v309H837l-41-41z" fill="var(--panel-c)"/>
  <g>
    <circle cx="402" cy="950" r="29" fill="#fff"/><circle cx="402" cy="950" r="25" fill="#4b72b4"/>
    <path d="M388 950h24M402 938l12 12-12 12" stroke="#fff" stroke-width="5" fill="none"/>
    <circle cx="787" cy="950" r="29" fill="#fff"/><circle cx="787" cy="950" r="25" fill="#4b72b4"/>
    <path d="M773 950h24M787 938l12 12-12 12" stroke="#fff" stroke-width="5" fill="none"/>
  </g>
</svg>

<section class="abs panel" style="left:25px;width:379px"><h2>ACCOUNT LOG IN</h2></section>
<div class="abs field" style="top:722px">user name</div>
<div class="abs field" style="top:807px">pass word</div>
<div class="abs signin">SIGN IN</div>
<div class="abs step" style="left:284px;top:936px">Go to next step</div>

<section class="abs panel" style="left:410px;width:380px"><h2>BRIEF SURVEY</h2></section>
<p class="abs survey-text">Sections 1.10.32 and 1.10.33 from "de Finibus Bonorum et Malorum" by Marcus Vell are also reproduced in their exact original form, accompanied by English versions from the 1914 translation by J. Tornby.</p>
<div class="abs more">View more...</div>
<div class="abs step" style="left:669px;top:936px">Go to next step</div>

<section class="abs panel" style="left:796px;width:379px"><h2>E - BOOK</h2></section>
<div class="abs ebook-icon" role="img" aria-label="Dark hardcover book icon"></div>
<div class="abs receive">Receive a copy of<br>Your E-Book</div>
<p class="abs receive-note">Marcus Vell are also reproduced in their exact original form, accompanied by English</p>
<div class="abs get">GET A COPY</div>

<footer class="abs footer"></footer>
<div class="abs copyright">Copyright @ 2011 www.piecebypiecehelp.com All rights reserved</div>
<div class="abs connect">Connect with us :</div>
<div class="abs social" style="left:947px">Friendsy</div>
<div class="abs social" style="left:995px">Chirply</div>
<div class="abs social" style="left:1043px">RSS</div>
<div class="abs social" style="left:1091px">Stackly</div>
</body>
</html>
```